New Website for World Wide Charity (KELVOR)

We need a dynamic web design for our brand new charity organisation that will be working worldwide. We will be funded by donations so need to attract people to donate.

What We Do
We work to optimise the wellbeing of the planet, the animals and all that live within. Our slogan is Achieving Vibrational Equilibrium.

We have included a Powerpoint document which may help you understand what we need, it is just an idea for structure and style, it is not set in stone so feel free to be as creative as you like!
Updates

Designs look the same

Target Market(s)

Adults 18+ with an interest in animal, environmental. Businesses that may like to support our natural world or already support our natural world.

Number of Pages Required

3 page

Colors

Designer to choose colors to be used in the design.

Requirements
Must have
• We need the website to be easy to use and understand.

Web pages will be Home, What We Do, Who We Are, Success Stories, What You Can Do (Blog section), Seek Help, Donate, Join.
Nice to have
• Natural feel, easy to navigate, Ideally the website will look natural and organic.

Natural colours, blues, greens, sand, gold, brown, grey, silver, Orange and yellow for impact.
Should not have
• Should not have a dark coloured theme.

```html
<!DOCTYPE html>
<html lang="en">
<head>
<meta charset="utf-8">
<title>KELVOR — Charity For Humanity</title>
<link href="https://fonts.googleapis.com/css2?family=Permanent+Marker&family=Poppins:wght@400;500;600&display=swap" rel="stylesheet">
<style>
:root{
  --green:#0f7d4f;
  --green-soft:#1a8a5a;
  --ink:#1d1d1f;
  --text:#555a60;
  --muted:#8b9096;
  --light:#f4f6f8;
  --navy:#17162f;
  --white:#ffffff;
  --gold:#f5b51c;
}
*{margin:0;padding:0;box-sizing:border-box}
html,body{width:1200px;height:4866px;overflow:hidden}
body{position:relative;font-family:"Poppins",sans-serif;color:var(--ink);background:var(--white)}
.abs{position:absolute}
.display{font-family:"Permanent Marker",cursive;font-weight:400;letter-spacing:1px}
.display em{font-style:normal;color:var(--green)}
.eyebrow{font-size:15px;font-weight:500;color:var(--green);text-align:center;width:1200px;left:0}
.section-title{font-size:34px;text-align:center;width:1200px;left:0;line-height:45px}
.btn{display:flex;align-items:center;justify-content:center;background:var(--green);color:var(--white);font-size:14px;font-weight:600}
.brand{display:flex;align-items:center;justify-content:center;border-radius:50%;background:var(--white);font-size:13px;font-weight:600;color:var(--navy)}

/* hero */
.hero{left:0;top:0;width:1200px;height:593px;background:linear-gradient(90deg,#2a1e15 0%,#4a3020 40%,#5a3a22 60%,#6f8b84 85%,#8aa29c 100%)}
.nav a{position:absolute;top:27px;font-size:12px;color:var(--white);text-decoration:none;white-space:nowrap}
.nav-dot{left:405px;top:52px;width:6px;height:6px;border-radius:50%;background:var(--green-soft)}
.login{left:930px;top:15px;width:89px;height:36px;font-size:12px}
.social{left:77px;width:28px;height:28px;border:1.5px solid var(--white);border-radius:50%}
.social::after{content:"";position:absolute;left:9px;top:9px;width:7px;height:7px;border-radius:50%;background:var(--white)}
.hero-title{left:183px;top:155px;font-size:58px;line-height:68px;color:var(--white)}
.hero-sub{left:183px;top:316px;font-size:17px;line-height:27px;color:var(--white);width:360px}
.donate{left:183px;top:406px;width:150px;height:49px}

/* cards */
.card{background:var(--white);box-shadow:0 6px 30px rgba(0,0,0,.07);border-radius:4px}
.card h3{position:absolute;font-size:20px;font-weight:600;white-space:nowrap}
.card p{position:absolute;font-size:11px;line-height:18px;color:var(--text)}
.readmore{position:absolute;font-size:14px;font-weight:500;display:flex;align-items:center;gap:16px;white-space:nowrap}
.readmore i{width:17px;height:17px;border-radius:50%;background:var(--green);display:inline-block}

/* about */
.about{left:0;top:1242px;width:1200px;height:567px;background:var(--light)}
.photo{border-radius:2px}

/* cause */
.cause{background:#f9f9f9}
.cause .body{left:30px;top:290px;width:205px;font-size:12px;line-height:21px}
.cause .meta{position:absolute;left:30px;top:226px;width:auto;white-space:nowrap;font-size:13px;line-height:18px;color:var(--ink)}
.cause .meta b{color:var(--green);font-weight:500}
.cause .meta .goal{margin-left:20px}
.cause h3{left:30px;top:252px}
.cause .link{position:absolute;left:30px;top:381px;font-size:13px;font-weight:600;color:var(--green)}

/* band */
.band{left:0;top:2585px;width:1200px;height:256px;background:linear-gradient(90deg,#147a4e,#0f7d4f 60%,#138355)}

/* testimonials */
.stars{position:absolute;left:35px;top:40px;color:var(--gold);font-size:14px;letter-spacing:1px}
.quote{position:absolute;left:35px;top:80px;width:200px;font-size:13px;line-height:23px;color:var(--text)}
.avatar{position:absolute;border-radius:50%;background:linear-gradient(135deg,#c9b8a4,#6f5c4c)}
.who{position:absolute;font-size:13px;font-weight:500;white-space:nowrap}
.who small{display:block;font-size:9px;color:var(--muted);font-weight:400}

/* blog */
.post .date{position:absolute;font-size:12px;color:var(--text)}
.post h4{position:absolute;font-size:17px;line-height:23px;font-weight:500;width:265px}
.post p{position:absolute;font-size:12px;line-height:20px;color:var(--text);width:250px}
.post .link{position:absolute;font-size:14px;color:var(--green);font-weight:500}

/* footer */
.footer{left:0;top:4200px;width:1200px;height:666px;background:var(--navy);color:var(--white)}
.news-title{left:181px;top:83px;font-size:32px;line-height:42px}
.news-field{left:605px;top:77px;width:408px;height:70px;border-radius:35px;background:var(--white)}
.news-field span{position:absolute;left:46px;top:26px;font-size:13px;color:#9a9aa5}
.news-field .btn{position:absolute;right:9px;top:11px;width:106px;height:48px;border-radius:24px;font-size:15px}
.rule{height:1px;background:rgba(255,255,255,.15)}
.col h5{position:absolute;font-size:19px;font-weight:600}
.col a{position:absolute;font-size:11px;color:var(--white);text-decoration:none;white-space:nowrap}
.foot-about{left:183px;top:401px;width:260px;font-size:11px;line-height:19px}
.foot-social{width:12px;height:12px;border-radius:50%;background:var(--white)}
.copy{left:0;width:1200px;top:627px;text-align:center;font-size:11px}
</style>
</head>
<body>

<!-- Hero -->
<header class="hero abs" role="img" aria-label="Photograph of a child peeking from behind a weathered wooden door"></header>
<div class="brand abs" style="left:183px;top:4px;width:87px;height:85px">KELVOR</div>
<nav class="nav">
  <a style="left:391px">Home</a>
  <a style="left:448px">What We Do</a>
  <a style="left:544px">Who We Are</a>
  <a style="left:641px">Success Stories</a>
  <a style="left:750px">Blog</a>
  <a style="left:800px">Donate</a>
  <a style="left:862px">Join</a>
</nav>
<div class="nav-dot abs"></div>
<div class="btn login abs">Login</div>
<div class="social abs" style="top:186px"></div>
<div class="social abs" style="top:237px"></div>
<div class="social abs" style="top:286px"></div>
<div class="social abs" style="top:337px"></div>
<div class="abs" style="left:91px;top:406px;width:1.5px;height:76px;background:var(--white)"></div>
<h1 class="hero-title display abs">Charity For<br>Humanity</h1>
<p class="hero-sub abs">Lorem ipsum dolor sit amet consectetur adipi elit sed do eiusmod.</p>
<div class="btn donate abs">Make Donation</div>
<svg class="abs" style="left:1036px;top:513px" width="80" height="24" viewBox="0 0 80 24" fill="none" stroke="#fff" stroke-width="2.5"><path d="M14 3 5 12l9 9M61 3l9 9-9 9"/></svg>

<!-- What we do -->
<p class="eyebrow abs" style="top:656px">What We do</p>
<h2 class="section-title display abs" style="top:703px"><em>Donate</em> To People <em>In</em><br>Extreme <em>Need</em></h2>

<div class="card abs" style="left:183px;top:847px;width:263px;height:325px">
  <svg class="abs" style="left:38px;top:32px" width="52" height="60" viewBox="0 0 52 60" fill="none" stroke="#0f7d4f" stroke-width="2"><circle cx="26" cy="36" r="20"/><path d="M26 16V4M26 10c-6-6-12-4-12-4s2 6 12 4c6-6 12-4 12-4s-2 6-12 4"/></svg>
  <h3 style="left:38px;top:112px">Environment</h3>
  <p style="left:38px;top:158px;width:195px">Lorem ipsum dolor sit amet consectet ur adipisicing elit sed do eiusmod tempor incididunt ut labore et.</p>
  <div class="abs" style="left:38px;top:235px;width:195px;height:1px;background:#555"></div>
  <div class="readmore" style="left:38px;top:262px"><i></i>Read More</div>
</div>
<div class="card abs" style="left:470px;top:847px;width:261px;height:325px">
  <svg class="abs" style="left:36px;top:38px" width="48" height="48" viewBox="0 0 48 48" fill="none" stroke="#0f7d4f" stroke-width="2"><ellipse cx="24" cy="33" rx="10" ry="9"/><circle cx="10" cy="20" r="5"/><circle cx="18" cy="8" r="5"/><circle cx="31" cy="8" r="5"/><circle cx="39" cy="20" r="5"/></svg>
  <h3 style="left:36px;top:112px">Animal</h3>
  <p style="left:36px;top:158px;width:195px">Lorem ipsum dolor sit amet consectet ur adipisicing elit sed do eiusmod tempor incididunt ut labore et.</p>
  <div class="abs" style="left:36px;top:235px;width:195px;height:1px;background:#555"></div>
  <div class="readmore" style="left:36px;top:262px"><i></i>Read More</div>
</div>
<div class="card abs" style="left:756px;top:847px;width:261px;height:325px">
  <svg class="abs" style="left:36px;top:36px" width="40" height="52" viewBox="0 0 40 52" fill="none" stroke="#0f7d4f" stroke-width="2"><circle cx="20" cy="15" r="11"/><path d="M2 50c0-12 8-20 18-20s18 8 18 20"/></svg>
  <h3 style="left:36px;top:112px">Human</h3>
  <p style="left:36px;top:158px;width:195px">Lorem ipsum dolor sit amet consectet ur adipisicing elit sed do eiusmod tempor incididunt ut labore et.</p>
  <div class="abs" style="left:36px;top:235px;width:195px;height:1px;background:#555"></div>
  <div class="readmore" style="left:36px;top:262px"><i></i>Read More</div>
</div>

<!-- About -->
<section class="about abs"></section>
<div class="photo abs" style="left:110px;top:1323px;width:514px;height:486px;background:linear-gradient(90deg,#8e3328 0%,#c9c5bf 40%,#6f7359 60%,#d8d6d2 80%,#f4f6f8 100%)" role="img" aria-label="Photograph of a smiling couple standing together"></div>
<div class="abs" style="left:660px;top:1325px;width:120px;height:36px;background:var(--white);color:var(--green);font-size:13px;font-weight:500;display:flex;align-items:center;justify-content:center">About Us</div>
<h2 class="display abs" style="left:660px;top:1392px;font-size:30px;line-height:40px;white-space:nowrap">We Are In A <em>Mission</em> To<br><em>Help</em> Helpless</h2>
<p class="abs" style="left:660px;top:1493px;width:352px;font-size:13.5px;line-height:22.5px;color:var(--text)">Lorem ipsum dolor sit amet consectetur adipisi cing elit sed do eiusmod tempor incididunt ut labore et dolore magna aliqua. Ut enim ad minim veniam, quis nostrud exercitation ullamco laboris nisi ut aliquip ex ea commodo consequat. Duis aute irure dolor in reprehenderit.</p>
<div class="avatar abs" style="left:658px;top:1657px;width:67px;height:67px;border:3px solid var(--white)" role="img" aria-label="Portrait of the charity founder"></div>
<p class="display abs" style="left:754px;top:1666px;font-size:20px;white-space:nowrap">John Doe</p>
<p class="abs" style="left:754px;top:1698px;font-size:13px;color:var(--muted)">Charity Founder</p>

<!-- Recent cause -->
<p class="eyebrow abs" style="top:1876px">Success Stories</p>
<h2 class="section-title display abs" style="top:1912px">Recent <em>Cause</em></h2>

<div class="card cause abs" style="left:183px;top:1992px;width:264px;height:427px">
  <div class="abs" style="left:0;top:0;width:264px;height:191px;background:linear-gradient(180deg,#9aa47a,#4f6a3e 60%,#3e5530)" role="img" aria-label="Photograph of a misty forest"></div>
  <p class="meta">Raised: <b>$40,000</b><span class="goal">Goal: $70,000</span></p>
  <h3>Environment</h3>
  <p class="body">Lorem ipsum dolor sit amet, cons ectetur adipisicing elit, sed do ei us mod tempor ut labore et dol ore magna aliqua.</p>
  <span class="link">Read More</span>
</div>
<div class="card cause abs" style="left:468px;top:1992px;width:264px;height:427px">
  <div class="abs" style="left:0;top:0;width:264px;height:191px;background:linear-gradient(180deg,#1e1a16,#3a2e22 60%,#8f7c5e)" role="img" aria-label="Photograph of puppies in a doorway"></div>
  <p class="meta">Raised: <b>$15,000</b><span class="goal">Goal: $30,000</span></p>
  <h3>Animal</h3>
  <p class="body">Lorem ipsum dolor sit amet, cons ectetur adipisicing elit, sed do ei us mod tempor ut labore et dol ore magna aliqua.</p>
  <span class="link">Read More</span>
</div>
<div class="card cause abs" style="left:753px;top:1992px;width:264px;height:427px">
  <div class="abs" style="left:0;top:0;width:264px;height:191px;background:linear-gradient(135deg,#5a3a26,#8d6547 50%,#b39077)" role="img" aria-label="Photograph of two smiling children"></div>
  <p class="meta">Raised: <b>$55,000</b><span class="goal">Goal: $90,000</span></p>
  <h3>Human</h3>
  <p class="body">Lorem ipsum dolor sit amet, cons ectetur adipisicing elit, sed do ei us mod tempor ut labore et dol ore magna aliqua.</p>
  <span class="link">Read More</span>
</div>
<div class="btn abs" style="left:533px;top:2464px;width:136px;height:51px">View More</div>

<!-- Join band -->
<section class="band abs" role="img" aria-label="Green-tinted photograph of children"></section>
<p class="abs" style="left:183px;top:2637px;font-size:13px;font-weight:500;color:var(--white)">Join With Us</p>
<h2 class="display abs" style="left:183px;top:2680px;font-size:34px;line-height:46px;color:var(--white);white-space:nowrap">Lets Change The World<br>With Humanity</h2>
<div class="abs" style="left:803px;top:2687px;width:214px;height:57px;background:var(--white);color:var(--green);font-size:13px;font-weight:600;display:flex;align-items:center;justify-content:center">Become A Volunteer</div>

<!-- Testimonials -->
<p class="eyebrow abs" style="top:2906px">Testimonials</p>
<h2 class="section-title display abs" style="top:2946px">What <em>People</em> Say</h2>

<div class="card abs" style="left:183px;top:3047px;width:263px;height:336px">
  <span class="stars">★★★★☆</span>
  <p class="quote">sed do eiusmod tempor incididunt ut labore et dolore magna aliqua. Ut enim ad minim veniam, quis nostrud exercitation ullamco laboris nisi ut aliquip ex eaommodo consequat.</p>
  <div class="avatar" style="left:35px;top:260px;width:38px;height:38px" role="img" aria-label="Reviewer portrait"></div>
  <p class="who" style="left:90px;top:260px">John Doe<small>Ceo</small></p>
</div>
<div class="card abs" style="left:468px;top:3047px;width:263px;height:336px">
  <span class="stars">★★★★☆</span>
  <p class="quote">Lorem ipsum dolor sit amet, consectetur adipisicing elit, sed do eiusmod tempor incididunt ut labore et dolore magna aliqua. Ut enim ad minim veniam, quis nostrud exercitation.</p>
  <div class="avatar" style="left:35px;top:260px;width:38px;height:38px" role="img" aria-label="Reviewer portrait"></div>
  <p class="who" style="left:90px;top:260px">John Doe<small>Ceo</small></p>
</div>
<div class="card abs" style="left:753px;top:3047px;width:263px;height:336px">
  <span class="stars">★★★★☆</span>
  <p class="quote">Lorem ipsum dolor sit amet, consectetur adipisicing elit, sed do eiusmod tempor incididunt ut labore et dolore magna aliqua. Ut enim ad minim veniam, quis nostrud exercitation.</p>
  <div class="avatar" style="left:35px;top:260px;width:38px;height:38px" role="img" aria-label="Reviewer portrait"></div>
  <p class="who" style="left:90px;top:260px">John Doe<small>Ceo</small></p>
</div>
<div class="abs" style="left:556px;top:3438px;width:18px;height:18px;border-radius:50%;background:var(--white);box-shadow:0 2px 8px rgba(0,0,0,.15)"></div>
<div class="abs" style="left:562px;top:3444px;width:6px;height:6px;border-radius:50%;background:var(--green)"></div>
<div class="abs" style="left:592px;top:3444px;width:6px;height:6px;border-radius:50%;background:#9aa"></div>
<div class="abs" style="left:615px;top:3444px;width:6px;height:6px;border-radius:50%;background:#9aa"></div>
<div class="abs" style="left:637px;top:3444px;width:6px;height:6px;border-radius:50%;background:#9aa"></div>

<!-- Blog -->
<p class="eyebrow abs" style="top:3524px">Our Blog</p>
<h2 class="section-title display abs" style="top:3562px">Recent <em>Events</em></h2>

<article class="post">
  <div class="abs" style="left:183px;top:3667px;width:263px;height:183px;background:linear-gradient(135deg,#7a4a2e,#c08850 45%,#4c6f9a)" role="img" aria-label="Photograph of a group of cheerful children"></div>
  <p class="date" style="left:183px;top:3870px">Date - 12.02.2021</p>
  <h4 style="left:183px;top:3896px">Lorem ipsum dolor sit amet, consectetur adipisicing.</h4>
  <p style="left:183px;top:3955px">Sed do eiusmod tempor incididunt ut labore et dolore magna aliqua.</p>
  <span class="link" style="left:183px;top:4007px">Read More</span>
</article>
<article class="post">
  <div class="abs" style="left:468px;top:3667px;width:263px;height:183px;background:linear-gradient(135deg,#dfe3e6,#8a929a 50%,#3b4046)" role="img" aria-label="Photograph of a vet treating an animal"></div>
  <p class="date" style="left:468px;top:3870px">Date - 12.02.2021</p>
  <h4 style="left:468px;top:3896px">Lorem ipsum dolor sit amet, consectetur adipisicing.</h4>
  <p style="left:468px;top:3955px">Sed do eiusmod tempor incididunt ut labore et dolore magna aliqua.</p>
  <span class="link" style="left:468px;top:4007px">Read More</span>
</article>
<article class="post">
  <div class="abs" style="left:753px;top:3667px;width:263px;height:183px;background:linear-gradient(135deg,#c9cbc8,#a48a6a 55%,#7c5d3e)" role="img" aria-label="Photograph of volunteers packing donation boxes"></div>
  <p class="date" style="left:753px;top:3870px">Date - 12.02.2021</p>
  <h4 style="left:753px;top:3896px">Lorem ipsum dolor sit amet, consectetur adipisicing.</h4>
  <p style="left:753px;top:3955px">Sed do eiusmod tempor incididunt ut labore et dolore magna aliqua.</p>
  <span class="link" style="left:753px;top:4007px">Read More</span>
</article>
<div class="btn abs" style="left:533px;top:4080px;width:136px;height:50px">View More</div>

<!-- Footer -->
<footer class="footer abs">
  <h2 class="news-title display abs">Get Update By Signup<br>Newsletter</h2>
  <div class="news-field abs"><span>Enter your email</span><div class="btn">Join</div></div>
  <div class="rule abs" style="left:183px;top:217px;width:834px"></div>

  <div class="brand abs" style="left:183px;top:283px;width:83px;height:81px">KELVOR</div>
  <p class="foot-about abs">Lorem ipsum dolor sit amet, consectetur adipiscing elit, sed do eiusmod tempor incididunt ut labore et dolore magna aliqua. Ut enim ad minim.</p>
  <div class="foot-social abs" style="left:183px;top:516px"></div>
  <div class="foot-social abs" style="left:216px;top:516px"></div>
  <div class="foot-social abs" style="left:249px;top:516px"></div>
  <div class="foot-social abs" style="left:282px;top:516px"></div>

  <div class="col">
    <h5 style="left:607px;top:288px">Charity</h5>
    <a style="left:607px;top:344px">Home</a>
    <a style="left:607px;top:383px">What We Do</a>
    <a style="left:607px;top:422px">Who We Are</a>
    <a style="left:607px;top:461px">Success Stories</a>
    <a style="left:607px;top:500px">Blog</a>
    <a style="left:607px;top:539px">Contact us</a>
  </div>
  <div class="col">
    <h5 style="left:758px;top:288px">Support</h5>
    <a style="left:758px;top:344px">Terms &amp; Policy</a>
    <a style="left:758px;top:383px">Privacy</a>
    <a style="left:758px;top:422px">Legal</a>
    <a style="left:758px;top:461px">Donet</a>
    <a style="left:758px;top:500px">Join</a>
  </div>
  <div class="col">
    <h5 style="left:911px;top:288px">Socials</h5>
    <a style="left:911px;top:344px">Newsfeed</a>
    <a style="left:911px;top:383px">Chirper</a>
    <a style="left:911px;top:422px">Snapshots</a>
    <a style="left:911px;top:461px">Portfolio</a>
  </div>

  <div class="rule abs" style="left:162px;top:595px;width:870px"></div>
  <p class="copy abs">Copyrights © 2020 - 2021 All Right Reserved</p>
</footer>

</body>
</html>
```